Label for Olive Oil Bottle SOMVETTA

Dear Designers,
The task is to create a label for an Olive Oil Bottle for the Somvetta Brand.
Please see the attached files for the information that must appear on the label.
Please produce the label in three different colour schemes: Red for the MERVO version of the label,
Blue for the SELTA version and light green for the DORVANTE version of the label.
Please present the label on photorealistic bottle bock-ups like shown in the file attached.
It is not necessary to use the same template but it must be similar.

Target Market(s)

Germany, Austria and Swizerland

Industry/Entity Type

Food Production

Font styles to use
Serif
Script

Requirements
Must have
• a) Please produce 3 different versions of the label:
• 1. MERVO
• 2. SELTA
• 3. DORVANTE
• b) Please use for the presentation of the labels the bottles in the attached file.
• They are in big scale so feel free to scale them down
• c) Please present the label on a white/transparent background
• d) Please fint the information for the labels on the files attached
Nice to have
• - Please see the file example.pdf to have a ROUGH idea how the design COULD be.
• - The label/mockup should be presented on a white/transparent background
Should not have
• Ill tell you...

```html
<!DOCTYPE html>
<html lang="de">
<head>
<meta charset="utf-8">
<title>Somvetta Olivenöl – Etiketten</title>
<link rel="stylesheet" href="https://fonts.googleapis.com/css2?family=Cinzel:wght@600;700&family=Libre+Baskerville:wght@400;700&family=Playball&display=swap">
<style>
  :root {
    --canvas: #f4f4f4;
    --green-light: #c3df6a;
    --green-mid: #9ccb45;
    --green-frame: #2f7d34;
    --red-light: #f0504a;
    --red-mid: #d8262b;
    --red-deep: #b71c1f;
    --blue-light: #bfeaf5;
    --blue-mid: #4cbfe0;
    --cream: #fff3c2;
    --gold: #f3d36b;
    --ink: #1d1d1b;
    --white: #ffffff;
    --olive-1: #b5d334;
    --olive-2: #5f8d1f;
    --leaf: #3e5c2a;
  }
  * { box-sizing: border-box; margin: 0; padding: 0; }
  html, body { width: 1200px; height: 1103px; overflow: hidden; }
  body {
    background: var(--canvas);
    font-family: "Libre Baskerville", Georgia, serif;
    position: relative;
  }

  .label {
    position: absolute;
    top: 250px;
    width: 230px;
    height: 600px;
    clip-path: polygon(14px 0, calc(100% - 14px) 0, 100% 14px, 100% calc(100% - 40px), 50% 100%, 0 calc(100% - 40px), 0 14px);
    background: radial-gradient(ellipse at 50% 40%, var(--label-glow) 0%, var(--label-bg) 70%);
    color: var(--label-text);
    text-align: center;
  }
  .label::before {
    content: "";
    position: absolute;
    inset: 6px;
    border: 2px solid var(--label-frame);
    clip-path: inherit;
    pointer-events: none;
  }
  .label--dorvante { left: 188px; --label-bg: var(--green-mid); --label-glow: var(--green-light); --label-frame: var(--green-frame); --label-text: var(--ink); --script: var(--red-mid); --script-sub: var(--red-mid); --variant: var(--red-mid); --band-bg: var(--red-mid); --band-text: var(--white); --origin: var(--ink); }
  .label--mervo { left: 467px; --label-bg: var(--red-mid); --label-glow: var(--red-light); --label-frame: var(--green-frame); --label-text: var(--cream); --script: var(--cream); --script-sub: var(--ink); --variant: var(--gold); --band-bg: var(--cream); --band-text: var(--red-deep); --origin: var(--cream); }
  .label--selta { left: 753px; --label-bg: var(--blue-mid); --label-glow: var(--blue-light); --label-frame: var(--green-frame); --label-text: var(--ink); --script: var(--ink); --script-sub: var(--ink); --variant: var(--ink); --band-bg: var(--red-mid); --band-text: var(--white); --origin: var(--red-mid); }

  .brand { padding-top: 26px; }
  .brand__name {
    font-family: "Libre Baskerville", Georgia, serif;
    font-weight: 700;
    font-size: 27px;
    letter-spacing: 1px;
    color: var(--red-deep);
  }
  .label--mervo .brand__name { color: var(--cream); }
  .brand__sub { font-size: 8px; letter-spacing: 1px; margin-top: 2px; }

  .title { position: relative; margin-top: 58px; font-family: "Playball", cursive; line-height: 1; }
  .title__olio { font-size: 66px; color: var(--script); }
  .title__extra { position: absolute; top: 52px; left: 112px; font-size: 12px; color: var(--script-sub); }
  .title__oliva { font-size: 30px; color: var(--script-sub); margin-top: -8px; }
  .label--dorvante .title__oliva { color: var(--red-mid); }

  .olive-art {
    width: 120px; height: 140px;
    margin: 22px auto 0;
    border-radius: 40% 60% 50% 50%;
    background: radial-gradient(circle at 40% 45%, var(--olive-1) 0%, var(--olive-2) 55%, var(--leaf) 100%);
  }

  .variant { margin: 26px 18px 0; border-top: 1px solid var(--variant); border-bottom: 1px solid var(--variant); padding: 4px 0 3px; }
  .variant__name { font-family: "Cinzel", serif; font-weight: 700; font-size: 22px; letter-spacing: 2px; color: var(--variant); }
  .origin { font-size: 7.5px; line-height: 1.15; margin-top: 8px; color: var(--origin); font-weight: 700; }
  .taste { font-family: "Cinzel", serif; font-size: 11px; font-weight: 700; margin-top: 8px; }
  .usage {
    display: inline-block;
    margin-top: 16px;
    padding: 3px 12px;
    background: var(--band-bg);
    color: var(--band-text);
    font-size: 11px;
    letter-spacing: 1px;
  }
  .label--selta .usage { margin-top: 4px; }
  .footer { display: flex; justify-content: space-between; align-items: center; margin: 20px 22px 0; font-size: 8px; }
  .footer__stars { color: var(--red-mid); font-size: 8px; letter-spacing: 1px; }
  .label--mervo .footer__stars { color: var(--gold); }
</style>
</head>
<body>
  <main class="label-set">
    <article class="label label--dorvante">
      <header class="brand">
        <div class="brand__name">SOMVETTA</div>
        <div class="brand__sub">OLIO D'OLIVA</div>
      </header>
      <div class="title">
        <div class="title__olio">Olio</div>
        <div class="title__extra">extra vergine</div>
        <div class="title__oliva">di oliva</div>
      </div>
      <div class="olive-art" role="img" aria-label="Illustration: zwei grüne Oliven an einem Zweig mit Blättern"></div>
      <div class="variant"><div class="variant__name">DORVANTE</div></div>
      <p class="origin">NATIVES OLIVENÖL EXTRA<br>AUS DER EUROPAISCHEN UNION</p>
      <div class="usage">IDEAL ZUM BRATEN</div>
      <div class="footer"><span>750ml e</span><span class="footer__stars">★★ ✦ ★★</span><span>BIS 220°C</span></div>
    </article>

    <article class="label label--mervo">
      <header class="brand">
        <div class="brand__name">SOMVETTA</div>
        <div class="brand__sub">OLIO D'OLIVA</div>
      </header>
      <div class="title">
        <div class="title__olio">Olio</div>
        <div class="title__oliva">di oliva</div>
      </div>
      <div class="olive-art" role="img" aria-label="Illustration: zwei grüne Oliven an einem Zweig mit Blättern"></div>
      <div class="variant"><div class="variant__name">MERVO</div></div>
      <p class="origin">NATIVES OLIVENÖL EXTRA<br>AUS DER EUROPAISCHEN UNION</p>
      <div class="usage">IDEAL ZUM BRATEN</div>
      <div class="footer"><span>750ml e</span><span class="footer__stars">★★ ✦ ★★</span><span>BIS 220°C</span></div>
    </article>

    <article class="label label--selta">
      <header class="brand">
        <div class="brand__name">SOMVETTA</div>
        <div class="brand__sub">OLIO D'OLIVA</div>
      </header>
      <div class="title">
        <div class="title__olio">Olio</div>
        <div class="title__extra">extra vergine</div>
        <div class="title__oliva">di oliva</div>
      </div>
      <div class="olive-art" role="img" aria-label="Illustration: zwei grüne Oliven an einem Zweig mit Blättern"></div>
      <div class="variant"><div class="variant__name">SELTA</div></div>
      <p class="origin">NATIVES OLIVENÖL EXTRA<br>AUS DER EUROPAISCHEN UNION</p>
      <div class="taste">MILD</div>
      <div class="usage">IDEAL FUR SALATE</div>
      <div class="footer"><span>750ml e</span><span class="footer__stars">★★ ✦ ★★</span><span>BIS 220°C</span></div>
    </article>
  </main>
</body>
</html>
```